Crowdsourced Research Platform: KOVAL Polls

KOVAL Polls is an acronym for Kindred Opinion Views Among Lands (KOVAL) Polls. This is a research effort to format and combine multiple sources of public opinion data from around the world into merged datasets. The website will at first mainly act as a quality control hub and distribution point for official dataset releases. It will provide resources such as codebooks, development guidelines, and instructional videos for crowdsourcing continued expansion of the resource. We need a coded (HTML and CSS) website design and associated files to launch the website with ease. We purchased the domain www.kovalpolls.org, but access is blocked while it is under construction.

The website design should be based on a logo recently commissioned (see attached). The design should be simple and professional with lots of white space. We would like the logo on the top left of all pages and the primary navigation menu along the top-right of all pages. The primary navigation menu should have a simple mouse-over effect and the main menu items should expand with secondary drop-down options. The footer should include a few columns with headings and links to different pages. The website layout should be dynamic and expand its width to fit different sized screens. There will be a lot of data and information displayed in tables, so we would like the CSS coding and website design to include tables designed to match the website theme. The main graphical content will be data visualisations such as pie/bar charts, histograms, scatter plots, heat maps, moving average trend lines etc. We would therefore like the design to include modular sections (boxes matching theme to display plots/graphs/etc) that can visually display these types of figures with text/caption underneath to explain the data visualizations.

For more information and written placeholder content, designers should read the attached documents to get a better idea about the project. Some draft working papers using merged datsets have been included for reference and you can use these for their examples of data visualizations and use the written content for filling in page content.

Target Market(s)

The primary target audience will be academics in universities and research institutes. The resource will be most useful to quantitative social scientists, particularly political scientists and sociologists, but any discipline concerned with us humans could find the resource useful. Others such as graduate-level university students, civil servants in government departments, members of research institutions, and policy researchers in non-profit organizations will also find the resource useful.

Coding

Coded - Design and coding required

Number of Pages Required

3 page

Font styles to use
Sans Serif

Colors

Designer to choose colors to be used in the design.

Requirements
Must have
• HTML and CSS coding (not Wordpress)
Nice to have
• Content boxes to display data visualizations alongside articles.

```html
<!DOCTYPE html>
<html lang="en">
<head>
<meta charset="utf-8">
<title>KOVAL Polls</title>
<link href="https://fonts.googleapis.com/css2?family=Roboto:wght@300;400;500;700&display=swap" rel="stylesheet">
<style>
:root{
  --brand:#1aa3de;
  --brand-deep:#0a72b9;
  --chart-blue:#1266f1;
  --navy:#243a5e;
  --teal:#35cbd3;
  --pale-teal:#c4e6ec;
  --steel:#4b86a8;
  --ink:#1c1c1c;
  --muted:#555;
  --rule:#e3e3e3;
  --footer:#1b1b1b;
  --white:#fff;
}
*{box-sizing:border-box;margin:0;padding:0}
html,body{width:1200px;height:4074px;overflow:hidden;background:var(--white)}
body{font-family:"Roboto",Arial,sans-serif;color:var(--ink);position:relative}
.abs{position:absolute}
.p{font-size:12.5px;line-height:1.45;color:#333}
.p + .p{margin-top:14px}
.heading{font-size:22px;font-weight:700;color:var(--ink)}
.heading::after{content:"";display:block;width:150px;height:3px;background:var(--ink);margin-top:12px}
.heading.right::after{margin-left:auto}
.divider{left:61px;width:1080px;height:1px;background:var(--rule)}

/* header */
.site-header{top:0;left:0;width:1200px;height:83px}
.logo{left:61px;top:24px;display:flex;align-items:center;gap:10px;color:var(--brand);font-weight:700;font-size:25px}
.logo-dot{width:30px;height:30px;border-radius:50%;background:var(--brand)}
.main-nav{right:64px;top:38px;display:flex;gap:26px;font-size:12px;color:#333;text-transform:uppercase}
.main-nav a{color:inherit;text-decoration:none;padding-bottom:4px}
.main-nav a.current{border-bottom:2px solid var(--ink)}

/* hero */
.hero{top:83px;left:0;width:1200px;height:549px;background:linear-gradient(110deg,#7f8e99 0%,#b9c4cc 40%,#5c7890 70%,#2f5a7e 100%)}
.hero-title{right:59px;top:175px;text-align:right;color:var(--white);font-size:46px;font-weight:700;line-height:1.12}
.hero-text{right:59px;top:325px;width:360px;text-align:right;color:var(--white);font-size:12px;line-height:1.4}
.btn{display:inline-block;background:var(--brand);color:var(--white);font-size:15px;font-weight:500;text-align:center}
.hero .btn{position:absolute;right:59px;top:418px;width:124px;height:40px;line-height:40px}

/* intro */
.intro{top:670px;left:0;width:1200px;text-align:center}
.intro h2{font-size:22px;font-weight:700}
.intro h2::after{content:"";display:block;width:240px;height:3px;background:var(--ink);margin:12px auto 0}
.intro .p{width:520px;margin:28px auto 0}

/* steps band */
.steps{top:831px;left:0;width:1200px;height:161px;background:var(--brand)}
.step{top:28px;width:120px;text-align:center;color:var(--white);font-size:11px;font-weight:500}
.step svg{display:block;margin:0 auto 20px}

/* feature sections */
.chart-axis text{font-size:11px;fill:#777;font-family:"Roboto",Arial,sans-serif}

/* cta */
.cta{top:2654px;left:0;width:1200px;height:144px;background:var(--brand-deep)}
.cta .p{color:var(--white);position:absolute;left:152px;top:42px;width:700px;font-size:12.5px}
.cta .btn{position:absolute;left:922px;top:52px;width:132px;height:40px;line-height:40px}
.stem{width:3px;background:var(--teal);left:600px}

/* overview */
.overview-title{top:2862px;left:0;width:1200px;text-align:center;color:var(--teal);font-size:32px;font-weight:300}
.overview-sub{top:2918px;left:0;width:1200px;text-align:center;font-size:12.5px;line-height:1.7;text-transform:uppercase;color:#333}
.mini{top:2980px;width:390px;height:262px}
.mini text{font-size:13px;fill:#444;font-family:"Roboto",Arial,sans-serif}
.point{top:3262px;width:340px;display:flex;gap:18px}
.point-num{font-size:56px;font-weight:300;color:var(--teal);line-height:1}
.point h3{font-size:22px;font-weight:400;margin:6px 0 8px}
.point p{font-size:14px;line-height:1.45;color:#333}
.company{top:3420px;left:61px;display:flex;align-items:center;gap:10px;font-size:10px;text-transform:uppercase}
.company-right{top:3424px;right:64px;font-size:10px;text-transform:uppercase}

/* contact */
.contact-title{top:3500px;left:61px;font-size:38px;font-weight:700}
.contact-title::after{content:"";display:block;width:210px;height:4px;background:var(--brand);margin-top:6px}
.field{font-size:16px;color:#666;border-bottom:1px solid #bbb;padding-bottom:14px}
.contact .btn{position:absolute;left:61px;top:3798px;width:180px;height:38px;line-height:38px;font-size:14px}

/* footer */
.site-footer{top:3878px;left:0;width:1200px;height:196px;background:var(--footer);color:#aaa}
.site-footer .logo{top:48px}
.foot-col{top:48px;width:120px;font-size:9.5px;line-height:1.5;color:#999}
.foot-col h4{color:var(--brand);font-size:10px;font-weight:500;margin-bottom:4px}
.follow{top:48px;left:992px;color:#ccc;font-size:15px}
.follow-icons{display:flex;gap:10px;margin-top:10px}
.follow-icons span{width:26px;height:26px;border-radius:50%;background:var(--brand)}
.copyright{top:166px;left:0;width:1200px;text-align:center;font-size:10px;color:#666}
</style>
</head>
<body>

<header class="site-header abs">
  <div class="logo abs"><span class="logo-dot"></span>KOVAL Polls</div>
  <nav class="main-nav abs">
    <a class="current" href="#">Home</a><a href="#">About Us</a><a href="#">Features</a><a href="#">Services</a><a href="#">Contact Us</a>
  </nav>
</header>

<section class="hero abs" role="img" aria-label="Photo of business people standing together in front of a city skyline with a glowing world network overlay">
  <h1 class="hero-title abs">Lorem ipsum dolor sit amet,<br>consectetur adipiscing elit.</h1>
  <p class="hero-text abs">Integer eu pretium neque, et efficitur nunc. Etiam sed facilisis lorem, nec vehicula eros. Phasellus dictum massa odio, at congue mauris condimentum quis. Donec sed lacinia nulla, ac pharetra eros. Aliquam bibendum vulputate suscipit.</p>
  <span class="btn">Click Here!</span>
</section>

<section class="intro abs">
  <h2>Lorem ipsum dolor sit amet</h2>
  <p class="p">Integer eu pretium neque, et efficitur nunc. Etiam sed facilisis lorem, nec vehicula eros. Phasellus dictum massa odio, at congue mauris condimentum quis. Donec sed lacinia nulla, ac pharetra eros. Aliquam bibendum vulputate suscipit.</p>
</section>

<section class="steps abs">
  <div class="step abs" style="left:245px">
    <svg width="70" height="70" viewBox="0 0 70 70" fill="none" stroke="#fff" stroke-width="3"><path d="M8 20h20l5 6h29v34H8z"/><path d="M14 14h16l4 5"/></svg>Step 1</div>
  <div class="step abs" style="left:438px">
    <svg width="70" height="70" viewBox="0 0 70 70" fill="none" stroke="#fff" stroke-width="3"><path d="M20 34a12 12 0 0 1 4-23 15 15 0 0 1 28 6 9 9 0 0 1-2 17z"/><rect x="20" y="38" width="30" height="8"/><rect x="20" y="48" width="30" height="8"/><path d="M35 56v8M24 64h22"/></svg>Step 2</div>
  <div class="step abs" style="left:633px">
    <svg width="70" height="70" viewBox="0 0 70 70" fill="none" stroke="#fff" stroke-width="3"><rect x="24" y="6" width="32" height="42"/><rect x="18" y="12" width="32" height="42" fill="#1aa3de"/><rect x="12" y="18" width="32" height="46" fill="#1aa3de"/><path d="M18 30h20M18 38h20M18 46h20M18 54h14"/></svg>Step 3</div>
  <div class="step abs" style="left:827px">
    <svg width="70" height="70" viewBox="0 0 70 70" fill="none" stroke="#fff" stroke-width="3"><path d="M22 46H16a12 12 0 0 1 2-24 17 17 0 0 1 32 2 11 11 0 0 1 2 22h-6"/><path d="M35 32v30M26 53l9 9 9-9"/></svg>Step 4</div>
</section>

<!-- Feature 1 -->
<section>
  <h2 class="heading abs" style="left:61px;top:1044px">Lorem ipsum dolor sit amet</h2>
  <div class="abs" style="left:61px;top:1104px;width:535px">
    <p class="p">Integer eu pretium neque, et efficitur nunc. Etiam sed facilisis lorem, nec vehicula eros. Phasellus dictum massa odio, at congue mauris condimentum quis. Donec sed lacinia nulla, ac pharetra eros. Aliquam bibendum vulputate suscipit. Nunc finibus nulla porttitor eros tempor rhoncus. Vestibulum lacinia odio vel arcu accumsan iaculis. Suspendisse potenti. Phasellus varius sem a velit pellentesque, eu scelerisque magna dignissim.</p>
    <p class="p">Aliquam erat volutpat. Nulla tristique hendrerit nulla, nec faucibus purus vehicula eget. Morbi a justo sed quam eleifend vehicula. Nulla sed nisl in nunc suscipit posuere a eget nulla. Donec nunc lorem, accumsan a aliquet in, dignissim quis ex. Mauris quis fermentum tortor, eu lacinia mi. Praesent sed sollicitudin tellus.</p>
    <p class="p">Ut eget nisl eget libero gravida rutrum. Ut id est scelerisque sapien maximus posuere ut vitae diam. Nunc dignissim, lacus ac commodo accumsan, ante eros molestie lorem, a blandit ligula urna id sem. Mauris rhoncus nibh a ornare iaculis. Maecenas congue mattis magna vitae elementum. Fusce vehicula dapibus nunc ac porttitor.</p>
  </div>
  <svg class="abs chart-axis" style="left:630px;top:1095px" width="520" height="260" viewBox="0 0 520 260">
    <g stroke="#eee"><line x1="40" y1="10" x2="510" y2="10"/><line x1="40" y1="52" x2="510" y2="52"/><line x1="40" y1="94" x2="510" y2="94"/><line x1="40" y1="136" x2="510" y2="136"/><line x1="40" y1="178" x2="510" y2="178"/></g>
    <line x1="40" y1="220" x2="510" y2="220" stroke="#999"/>
    <g text-anchor="end"><text x="32" y="14">1000</text><text x="32" y="56">800</text><text x="32" y="98">600</text><text x="32" y="140">400</text><text x="32" y="182">200</text><text x="32" y="224">0</text></g>
    <g fill="var(--chart-blue)">
      <rect x="50" y="15" width="20" height="205"/><rect x="88" y="118" width="20" height="102"/><rect x="126" y="90" width="20" height="130"/><rect x="164" y="60" width="20" height="160"/><rect x="202" y="90" width="20" height="130"/><rect x="240" y="134" width="20" height="86"/><rect x="278" y="63" width="20" height="157"/><rect x="316" y="40" width="20" height="180"/><rect x="354" y="194" width="20" height="26"/><rect x="392" y="40" width="20" height="180"/><rect x="430" y="190" width="20" height="30"/><rect x="468" y="72" width="20" height="148"/>
    </g>
    <g text-anchor="middle"><text x="60" y="242">100</text><text x="98" y="242">200</text><text x="136" y="242">300</text><text x="174" y="242">400</text><text x="212" y="242">500</text><text x="250" y="242">600</text><text x="288" y="242">700</text><text x="326" y="242">800</text><text x="364" y="242">900</text><text x="402" y="242">1000</text><text x="440" y="242">1100</text><text x="478" y="242">1200</text></g>
  </svg>
  <div class="divider abs" style="top:1399px"></div>
</section>

<!-- Feature 2 -->
<section>
  <h2 class="heading right abs" style="right:59px;top:1435px;text-align:right">Lorem ipsum dolor sit amet</h2>
  <svg class="abs" style="left:92px;top:1470px" width="430" height="290" viewBox="0 0 430 290" font-family="Roboto, Arial, sans-serif" font-size="28" text-anchor="middle">
    <g fill="none" stroke-width="11" transform="rotate(-90)">
      <circle cx="-65" cy="65" r="56" stroke="var(--pale-teal)"/><circle cx="-65" cy="65" r="56" stroke="var(--chart-blue)" stroke-dasharray="88 352"/>
      <circle cx="-65" cy="210" r="56" stroke="var(--pale-teal)"/><circle cx="-65" cy="210" r="56" stroke="var(--teal)" stroke-dasharray="176 352"/>
      <circle cx="-65" cy="355" r="56" stroke="var(--pale-teal)"/><circle cx="-65" cy="355" r="56" stroke="var(--navy)" stroke-dasharray="229 352"/>
      <circle cx="-220" cy="65" r="56" stroke="var(--pale-teal)"/><circle cx="-220" cy="65" r="56" stroke="var(--teal)" stroke-dasharray="176 352"/>
      <circle cx="-220" cy="210" r="56" stroke="var(--pale-teal)"/><circle cx="-220" cy="210" r="56" stroke="var(--navy)" stroke-dasharray="229 352"/>
      <circle cx="-220" cy="355" r="56" stroke="var(--pale-teal)"/><circle cx="-220" cy="355" r="56" stroke="var(--steel)" stroke-dasharray="264 352"/>
    </g>
    <text x="65" y="75" fill="var(--chart-blue)">25%</text><text x="210" y="75" fill="var(--teal)">50%</text><text x="355" y="75" fill="var(--navy)">65%</text>
    <text x="65" y="230" fill="var(--teal)">50%</text><text x="210" y="230" fill="var(--navy)">65%</text><text x="355" y="230" fill="var(--steel)">75%</text>
  </svg>
  <div class="abs" style="left:637px;top:1495px;width:504px;text-align:right">
    <p class="p">Integer eu pretium neque, et efficitur nunc. Etiam sed facilisis lorem, nec vehicula eros. Phasellus dictum massa odio, at congue mauris condimentum quis. Donec sed lacinia nulla, ac pharetra eros. Aliquam bibendum vulputate suscipit. Nunc finibus nulla porttitor eros tempor rhoncus. Vestibulum lacinia odio vel arcu accumsan iaculis. Suspendisse potenti. Phasellus varius sem a velit pellentesque, eu scelerisque magna dignissim.</p>
    <p class="p">Aliquam erat volutpat. Nulla tristique hendrerit nulla, nec faucibus purus vehicula eget. Morbi a justo sed quam eleifend vehicula. Nulla sed nisl in nunc suscipit posuere a eget nulla. Donec nunc lorem, accumsan a aliquet in, dignissim quis ex. Mauris quis fermentum tortor, eu lacinia mi. Praesent sed sollicitudin tellus.</p>
    <p class="p">Ut eget nisl eget libero gravida rutrum. Ut id est scelerisque sapien maximus posuere ut vitae diam. Nunc dignissim, lacus ac commodo accumsan, ante eros molestie lorem, a blandit ligula urna id sem. Mauris rhoncus nibh a ornare iaculis. Maecenas congue mattis magna vitae elementum. Fusce vehicula dapibus nunc ac porttitor.</p>
  </div>
  <div class="divider abs" style="top:1800px"></div>
</section>

<!-- Feature 3 -->
<section>
  <h2 class="heading abs" style="left:61px;top:1838px">Lorem ipsum dolor sit amet</h2>
  <div class="abs" style="left:61px;top:1898px;width:535px">
    <p class="p">Integer eu pretium neque, et efficitur nunc. Etiam sed facilisis lorem, nec vehicula eros. Phasellus dictum massa odio, at congue mauris condimentum quis. Donec sed lacinia nulla, ac pharetra eros. Aliquam bibendum vulputate suscipit. Nunc finibus nulla porttitor eros tempor rhoncus. Vestibulum lacinia odio vel arcu accumsan iaculis. Suspendisse potenti. Phasellus varius sem a velit pellentesque, eu scelerisque magna dignissim.</p>
    <p class="p">Aliquam erat volutpat. Nulla tristique hendrerit nulla, nec faucibus purus vehicula eget. Morbi a justo sed quam eleifend vehicula. Nulla sed nisl in nunc suscipit posuere a eget nulla. Donec nunc lorem, accumsan a aliquet in, dignissim quis ex. Mauris quis fermentum tortor, eu lacinia mi. Praesent sed sollicitudin tellus.</p>
    <p class="p">Ut eget nisl eget libero gravida rutrum. Ut id est scelerisque sapien maximus posuere ut vitae diam. Nunc dignissim, lacus ac commodo accumsan, ante eros molestie lorem, a blandit ligula urna id sem. Mauris rhoncus nibh a ornare iaculis. Maecenas congue mattis magna vitae elementum. Fusce vehicula dapibus nunc ac porttitor.</p>
  </div>
  <svg class="abs" style="left:770px;top:1860px" width="380" height="325" viewBox="0 0 380 325" font-family="Roboto, Arial, sans-serif" font-size="14">
    <g stroke="#eee"><line x1="50" y1="12" x2="370" y2="12"/><line x1="50" y1="70" x2="370" y2="70"/><line x1="50" y1="128" x2="370" y2="128"/><line x1="50" y1="186" x2="370" y2="186"/><line x1="50" y1="244" x2="370" y2="244"/></g>
    <line x1="50" y1="12" x2="50" y2="302" stroke="#999"/><line x1="50" y1="302" x2="370" y2="302" stroke="#999"/>
    <g fill="#666" text-anchor="end"><text x="40" y="17">1000</text><text x="40" y="75">800</text><text x="40" y="133">600</text><text x="40" y="191">400</text><text x="40" y="249">200</text><text x="40" y="307">0</text></g>
    <rect x="82" y="157" width="60" height="145" fill="var(--chart-blue)"/>
    <rect x="182" y="99" width="60" height="203" fill="var(--teal)"/>
    <rect x="282" y="12" width="60" height="290" fill="var(--navy)"/>
    <g fill="#fff" font-size="13" text-anchor="middle"><text x="112" y="178">50%</text><text x="212" y="120">50%</text><text x="312" y="34">100%</text></g>
    <g fill="#666" text-anchor="middle"><text x="112" y="324">2016</text><text x="212" y="324">2017</text><text x="312" y="324">2018</text></g>
  </svg>
  <div class="divider abs" style="top:2230px"></div>
</section>

<!-- Feature 4 -->
<section>
  <svg class="abs chart-axis" style="left:61px;top:2278px" width="520" height="300" viewBox="0 0 520 300">
    <g stroke="#eee"><line x1="40" y1="16" x2="510" y2="16"/><line x1="40" y1="58" x2="510" y2="58"/><line x1="40" y1="100" x2="510" y2="100"/><line x1="40" y1="142" x2="510" y2="142"/><line x1="40" y1="184" x2="510" y2="184"/></g>
    <line x1="40" y1="226" x2="510" y2="226" stroke="#999"/>
    <g text-anchor="end"><text x="32" y="20">1000</text><text x="32" y="62">750</text><text x="32" y="104">500</text><text x="32" y="146">250</text><text x="32" y="188">100</text><text x="32" y="230">0</text></g>
    <polyline fill="none" stroke="var(--chart-blue)" stroke-width="2" points="50,165 92,205 134,165 176,200 218,145 260,145 302,145 344,100 386,190 428,190 470,190 508,20"/>
    <polyline fill="none" stroke="var(--teal)" stroke-width="2" points="50,145 92,145 134,58 176,200 218,115 260,115 302,182 344,182 386,130 428,182 470,120"/>
    <polyline fill="none" stroke="#8bd3e8" stroke-width="1.5" points="50,190 200,170 350,150 508,110"/>
    <polyline fill="none" stroke="#c2e4ef" stroke-width="1.5" points="50,200 200,140 350,180 508,130"/>
    <g fill="var(--chart-blue)"><circle cx="50" cy="165" r="3.5"/><circle cx="92" cy="205" r="3.5"/><circle cx="134" cy="165" r="3.5"/><circle cx="176" cy="200" r="3.5"/><circle cx="218" cy="145" r="3.5"/><circle cx="302" cy="145" r="3.5"/><circle cx="344" cy="100" r="3.5"/><circle cx="386" cy="190" r="3.5"/><circle cx="428" cy="190" r="3.5"/><circle cx="508" cy="20" r="3.5"/></g>
    <g fill="var(--teal)"><circle cx="50" cy="145" r="3.5"/><circle cx="134" cy="58" r="3.5"/><circle cx="218" cy="115" r="3.5"/><circle cx="260" cy="115" r="3.5"/><circle cx="344" cy="182" r="3.5"/><circle cx="386" cy="130" r="3.5"/><circle cx="470" cy="120" r="3.5"/></g>
    <g text-anchor="middle"><text x="50" y="246">100</text><text x="92" y="246">200</text><text x="134" y="246">300</text><text x="176" y="246">400</text><text x="218" y="246">500</text><text x="260" y="246">600</text><text x="302" y="246">700</text><text x="344" y="246">800</text><text x="386" y="246">900</text><text x="428" y="246">1000</text><text x="470" y="246">1100</text><text x="508" y="246">1200</text></g>
    <rect x="40" y="262" width="6" height="24" fill="var(--chart-blue)"/>
    <text x="54" y="272" style="fill:var(--chart-blue)">Lorem ipsum dolor sit amet,</text><text x="54" y="285" style="fill:var(--chart-blue)">consectetuer adipiscing elit.</text>
    <rect x="280" y="262" width="6" height="24" fill="var(--teal)"/>
    <text x="294" y="272" style="fill:var(--teal)">Lorem ipsum dolor sit amet,</text><text x="294" y="285" style="fill:var(--teal)">consectetuer adipiscing elit.</text>
  </svg>
  <h2 class="heading right abs" style="right:59px;top:2268px;text-align:right">Lorem ipsum dolor sit amet</h2>
  <div class="abs" style="left:637px;top:2328px;width:504px;text-align:right">
    <p class="p">Integer eu pretium neque, et efficitur nunc. Etiam sed facilisis lorem, nec vehicula eros. Phasellus dictum massa odio, at congue mauris condimentum quis. Donec sed lacinia nulla, ac pharetra eros. Aliquam bibendum vulputate suscipit. Nunc finibus nulla porttitor eros tempor rhoncus. Vestibulum lacinia odio vel arcu accumsan iaculis. Suspendisse potenti. Phasellus varius sem a velit pellentesque, eu scelerisque magna dignissim.</p>
    <p class="p">Aliquam erat volutpat. Nulla tristique hendrerit nulla, nec faucibus purus vehicula eget. Morbi a justo sed quam eleifend vehicula. Nulla sed nisl in nunc suscipit posuere a eget nulla. Donec nunc lorem, accumsan a aliquet in, dignissim quis ex. Mauris quis fermentum tortor, eu lacinia mi. Praesent sed sollicitudin tellus.</p>
    <p class="p">Ut eget nisl eget libero gravida rutrum. Ut id est scelerisque sapien maximus posuere ut vitae diam. Nunc dignissim, lacus ac commodo accumsan, ante eros molestie lorem, a blandit ligula urna id sem. Mauris rhoncus nibh a ornare iaculis. Maecenas congue mattis magna vitae elementum. Fusce vehicula dapibus nunc ac porttitor.</p>
  </div>
</section>

<section class="cta abs">
  <p class="p">Integer eu pretium neque, et efficitur nunc. Etiam sed facilisis lorem, nec vehicula eros. Phasellus dictum massa odio, at congue mauris condimentum quis. Donec sed lacinia nulla, ac pharetra eros. Aliquam bibendum vulputate suscipit. Nunc finibus nulla porttitor eros tempor rhoncus. Vestibulum lacinia odio vel arcu accumsan iaculis. Suspendisse potenti. Phasellus varius sem a velit pellentesque, eu scelerisque magna dignissim.</p>
  <span class="btn">Click Here!</span>
</section>

<div class="stem abs" style="top:2798px;height:56px"></div>

<section class="overview">
  <h2 class="overview-title abs">LOREM IPSUM</h2>
  <p class="overview-sub abs">Lorem ipsum dolor sit amet, consectetur adipiscing elit,<br>sed diam nonummy nibh euismod tincidunt ut</p>

  <svg class="mini abs" style="left:75px" viewBox="0 0 390 262">
    <rect x="40" y="8" width="340" height="210" fill="none" stroke="#e6e6e6"/>
    <g stroke="#eee"><line x1="50" y1="47" x2="370" y2="47"/><line x1="50" y1="100" x2="370" y2="100"/><line x1="50" y1="152" x2="370" y2="152"/></g>
    <line x1="50" y1="205" x2="370" y2="205" stroke="#999"/>
    <g text-anchor="end"><text x="32" y="52">100</text><text x="32" y="105">75</text><text x="32" y="157">50</text><text x="32" y="210">25</text><text x="32" y="262">0</text></g>
    <rect x="100" y="115" width="9" height="90" fill="var(--teal)"/><rect x="150" y="115" width="9" height="90" fill="var(--teal)"/><rect x="200" y="57" width="9" height="148" fill="#4a9de0"/><rect x="250" y="115" width="9" height="90" fill="var(--teal)"/><rect x="300" y="70" width="9" height="135" fill="#4a9de0"/>
    <g text-anchor="middle"><text x="104" y="240">10</text><text x="154" y="240">20</text><text x="204" y="240">30</text><text x="254" y="240">40</text><text x="304" y="240">50</text></g>
  </svg>
  <svg class="mini abs" style="left:405px" viewBox="0 0 390 262">
    <rect x="40" y="8" width="340" height="210" fill="none" stroke="#e6e6e6"/>
    <line x1="50" y1="205" x2="370" y2="205" stroke="#999"/>
    <rect x="100" y="115" width="9" height="90" fill="var(--teal)"/><rect x="150" y="30" width="9" height="175" fill="#4a9de0"/><rect x="200" y="57" width="9" height="148" fill="#4a9de0"/><rect x="250" y="115" width="9" height="90" fill="var(--teal)"/><rect x="300" y="150" width="9" height="55" fill="#4a9de0"/>
    <g text-anchor="middle"><text x="104" y="240">10</text><text x="154" y="240">20</text><text x="204" y="240">30</text><text x="254" y="240">40</text><text x="304" y="240">50</text></g>
  </svg>
  <svg class="mini abs" style="left:735px" viewBox="0 0 390 262">
    <rect x="40" y="8" width="340" height="210" fill="none" stroke="#e6e6e6"/>
    <line x1="50" y1="205" x2="370" y2="205" stroke="#999"/>
    <rect x="100" y="115" width="9" height="90" fill="var(--teal)"/><rect x="150" y="83" width="9" height="122" fill="var(--teal)"/><rect x="200" y="165" width="9" height="40" fill="#4a9de0"/><rect x="250" y="115" width="9" height="90" fill="var(--teal)"/><rect x="300" y="57" width="9" height="148" fill="#4a9de0"/>
    <g text-anchor="middle"><text x="104" y="240">10</text><text x="154" y="240">20</text><text x="204" y="240">30</text><text x="254" y="240">40</text><text x="304" y="240">50</text></g>
  </svg>

  <div class="point abs" style="left:82px"><span class="point-num">01</span><div><h3>Lorem ipsum</h3><p>Lorem ipsum dolor sit amet, con-<br>sectetuer adipiscing elit,</p></div></div>
  <div class="point abs" style="left:443px"><span class="point-num">02</span><div><h3>Lorem ipsum</h3><p>Lorem ipsum dolor sit amet, con-<br>sectetuer adipiscing elit,</p></div></div>
  <div class="point abs" style="left:802px"><span class="point-num">03</span><div><h3>Lorem ipsum</h3><p>Lorem ipsum dolor sit amet, con-<br>sectetuer adipiscing elit,</p></div></div>

  <div class="company abs">
    <svg width="22" height="22" viewBox="0 0 22 22" fill="none" stroke="#222" stroke-width="1.5"><circle cx="11" cy="11" r="9"/><ellipse cx="11" cy="11" rx="4" ry="9"/><path d="M2 11h18M4 6h14M4 16h14"/></svg>
    Companyname
  </div>
  <div class="company-right abs">Lorem ipsum</div>
</section>

<div class="stem abs" style="top:3420px;height:56px"></div>

<section class="contact">
  <h2 class="contact-title abs">Contact Us</h2>
  <div class="field abs" style="left:69px;top:3606px;width:416px">Your name</div>
  <div class="field abs" style="left:568px;top:3606px;width:415px">Your name</div>
  <div class="field abs" style="left:69px;top:3662px;width:914px;height:106px">Message</div>
  <span class="btn">Submit</span>
</section>

<footer class="site-footer abs">
  <div class="logo abs" style="font-size:23px"><span class="logo-dot" style="width:26px;height:26px"></span>KOVAL Polls</div>
  <div class="foot-col abs" style="left:380px"><h4>Links</h4>About the data<br>Release notes<br>Codebooks<br>Guidelines<br>Tutorial videos<br>Methods<br>Data archive</div>
  <div class="foot-col abs" style="left:532px"><h4>Links</h4>Latest release<br>Dataset index<br>Working papers<br>Contributors<br>Quality control<br>Citation guide<br>Team members</div>
  <div class="foot-col abs" style="left:687px"><h4>Links</h4>Get involved<br>Submit data<br>Style guide<br>Questions<br>Newsletter<br>Partners<br>Contact details</div>
  <div class="follow abs">Follow Us<div class="follow-icons"><span></span><span></span><span></span><span></span></div></div>
  <p class="copyright abs">Copyright 2024 KOVAL Polls. All rights reserved.</p>
</footer>

</body>
</html>
```